Business Card Design Project

My business sells promotional merchandise to large blue chip companies. Gear like polo shirts, drink bottles, pens, basically anything that you can put a company logo onto.

I need the following elements included:
Logo as attached
Peter Hollingdale Managing Director
27 Corbel Street Tarrin Cove 4178
mobile 0438 514203
email kestrelpath@kestrelpathtrading.com.au

Promotional Merchandise with a difference

Target Market(s)

Mature age Marketing Managers

Industry/Entity Type

Business

```html
<!DOCTYPE html>
<html lang="en">
<head>
<meta charset="utf-8">
<title>Kestrel Path – Business Card</title>
<link rel="stylesheet" href="https://fonts.googleapis.com/css2?family=Cinzel:wght@700&family=Jost:wght@400;500;600&display=swap">
<style>
  :root {
    --board: #dcdddf;
    --navy: #06337a;
    --navy-deep: #0a2d66;
    --white: #ffffff;
    --ink: #4a4a4a;
    --label: #333333;
  }
  * { margin: 0; padding: 0; box-sizing: border-box; }
  html, body {
    width: 1058px;
    height: 1200px;
    overflow: hidden;
    background: var(--board);
    font-family: "Jost", "Futura", sans-serif;
  }
  .board { position: relative; width: 1058px; height: 1200px; }
  .side-label {
    position: absolute;
    left: 0;
    width: 1058px;
    text-align: center;
    font-family: "Cinzel", serif;
    font-weight: 700;
    font-size: 20px;
    letter-spacing: 1px;
    color: var(--label);
  }
  .side-label--front { top: 90px; }
  .side-label--back { top: 601px; }

  .card {
    position: absolute;
    left: 145px;
    width: 768px;
    height: 426px;
    overflow: hidden;
  }
  .card--front { top: 130px; background: var(--navy); }
  .card--back { top: 641px; background: var(--white); }

  .front-badge {
    position: absolute;
    left: 256px;
    top: 182px;
    width: 256px;
    height: 61px;
    background: var(--white);
    display: flex;
    align-items: center;
    justify-content: center;
  }
  .wordmark {
    font-family: "Jost", sans-serif;
    font-weight: 500;
    letter-spacing: 0.5px;
    line-height: 1;
    white-space: nowrap;
  }
  .front-badge .wordmark { color: var(--navy); font-size: 30px; }

  .front-echo {
    position: absolute;
    left: 0;
    bottom: 0;
    width: 768px;
    height: 110px;
  }
  .front-echo text {
    font-family: "Jost", sans-serif;
    font-weight: 500;
    fill: var(--navy-deep);
  }

  .back-band {
    position: absolute;
    left: 0;
    top: 43px;
    width: 320px;
    height: 59px;
    background: var(--navy);
    display: flex;
    align-items: center;
    justify-content: flex-end;
    padding-right: 16px;
  }
  .back-band .wordmark { color: var(--white); font-size: 31px; }

  .tagline {
    position: absolute;
    right: 430px;
    top: 112px;
    text-align: right;
    font-weight: 500;
    font-size: 13px;
    line-height: 18px;
    text-transform: uppercase;
    color: var(--navy);
  }

  .person {
    position: absolute;
    right: 449px;
    top: 252px;
    text-align: right;
  }
  .person__name {
    font-weight: 500;
    font-size: 31px;
    line-height: 38px;
    color: var(--navy);
  }
  .person__role {
    font-weight: 400;
    font-size: 19px;
    line-height: 26px;
    color: var(--ink);
  }

  .contact {
    position: absolute;
    right: 62px;
    top: 262px;
    text-align: right;
    font-style: normal;
    font-size: 16.5px;
    line-height: 22px;
    color: var(--ink);
  }
</style>
</head>
<body>
<main class="board">
  <div class="side-label side-label--front">FRONT</div>
  <section class="card card--front" aria-label="Card front">
    <div class="front-badge"><span class="wordmark">KESTRELPATH</span></div>
    <svg class="front-echo" viewBox="0 0 768 110" aria-hidden="true">
      <text x="0" y="128" font-size="146" textLength="768" lengthAdjust="spacingAndGlyphs">KESTRELPATH</text>
    </svg>
  </section>

  <div class="side-label side-label--back">BACK</div>
  <section class="card card--back" aria-label="Card back">
    <div class="back-band"><span class="wordmark">KESTRELPATH</span></div>
    <p class="tagline">Promotional merchandise<br>with a difference</p>
    <div class="person">
      <p class="person__name">Peter Hollingdale</p>
      <p class="person__role">Managing Director</p>
    </div>
    <address class="contact">
      27 Corbel Street Tarrin Cove 4178<br>
      M: 0438 514203<br>
      E: kestrelpath@kestrelpathtrading.com.au
    </address>
  </section>
</main>
</body>
</html>
```